Realtor / Real Estate Lead Generation site

Need a website design for lead generation. This website connects realtors with buyers and sellers of homes. some sites i like are: lumoquest.com, brixvale.com, quillmerows.com. Those sites look nice and have the same purpose as mine. The name of my site is VelnorHomeBridge. Basically I connect people with Top producing real estate agents
Updates

Project Deadline Extended Reason: Im still waiting on all my friends to pick the design. I have sent them the link to view and comment. I will be committing payment as well. Added Monday, February 15, 2016

Target Market(s)

people looking to buy or sell a home

Industry/Entity Type

Real Estate

Coding

Coded - Design and coding required

Number of Pages Required

5+ page

Font styles to use
Sans Serif

Requirements
Must have
• 2 versions of a lead capture form. One for buyers and one for sellers. goto www.quillmerows.com and select "buyer", you will see a for asking for Price Range, Type of Home, and City or Zipcode. If you select seller it has a differnt set of questions. I like the way they have trust builders on the right hand side such as realtors faces and comments about the realtors.I would like trust builders above the fold as well, so when its viewed on a phone or computer they can see them without scrolling, something such as #1 company, please see lumoquest-mobile.png file attached. I also have an explainer video that I would like a link to on the homepage above the fold without scrolling. please see darvikto.png file to see an example. I will upload video later. There should be a thank you page, privacy policy, terms and conditions. For ALL content see. www.789plotvista.com which is my current site.
• I would like the page to be mobile responsive/wordpress. Lastly, please see the form on 789plotvista.com. once you select the city, zipcode or address, and click "find my perfect agent, a form will come up with several different sets of questions. I would like that exact form used as I already paid for it on my other site. Thank you

```html
<!DOCTYPE html>
<html lang="en">
<head>
<meta charset="utf-8">
<title>VelnorHomeBridge</title>
<link href="https://fonts.googleapis.com/css2?family=Open+Sans:ital,wght@0,300;0,400;0,600;0,700;1,400&display=swap" rel="stylesheet">
<style>
:root{
  --orange:#e9a823;
  --blue:#1a6fb5;
  --ink:#333333;
  --muted:#666666;
  --line:#dddddd;
  --footer:#2b2b2b;
  --footer-text:#d4d4d4;
  --white:#ffffff;
}
*{box-sizing:border-box;margin:0;padding:0}
html,body{width:1200px;height:3005px;overflow:hidden;background:var(--white)}
body{position:relative;font-family:"Open Sans",Arial,sans-serif;color:var(--ink)}
.abs{position:absolute}

/* hero */
.hero{left:0;top:0;width:1200px;height:524px;background:linear-gradient(160deg,#3d4a3a 0%,#7a6048 35%,#c79a62 55%,#5a4636 75%,#2e3b2a 100%)}
.nav{left:86px;top:0;width:1026px;height:74px;background:rgba(30,30,30,.55);display:flex;align-items:center;padding:0 14px}
.brand{display:flex;align-items:center;gap:10px;color:var(--white);font-weight:700;font-size:14px}
.brand-mark{width:40px;height:40px;border-radius:50%;background:var(--blue);border:2px solid var(--white)}
.menu{margin-left:auto;display:flex;align-items:center;gap:18px;color:var(--white);font-size:12.5px;font-weight:700}
.menu .sign{font-weight:600;font-size:12px;display:flex;gap:6px;align-items:center}
.tab{top:146px;height:50px;width:188px;display:flex;align-items:center;justify-content:center;font-size:15px;font-weight:600}
.tab-buyers{left:184px;background:var(--blue);color:var(--white)}
.tab-sellers{left:374px;background:rgba(235,235,235,.92);color:var(--ink)}
.lead-form{left:184px;top:196px;width:832px;height:188px;background:rgba(255,255,255,.88)}
.lead-form h1{position:absolute;left:24px;top:24px;font-size:20px;font-weight:700;color:#222}
.field{position:absolute;height:40px;background:var(--white);border:1px solid var(--line);font-size:11px;color:#555;padding:0 14px;display:flex;align-items:center}
.btn-find{position:absolute;height:40px;background:var(--orange);color:var(--white);font-size:13px;font-weight:700;display:flex;align-items:center;justify-content:center}
.dots{display:flex;gap:6px}
.dot{width:14px;height:14px;border-radius:50%;border:2px solid var(--white)}
.dot.on{background:var(--orange);border-color:var(--orange)}

/* section titles */
.sec-title{left:0;width:1200px;text-align:center;font-size:21px;font-weight:400;letter-spacing:.3px}
.sec-title b{font-weight:700}
.swoosh{left:550px;width:100px;height:12px}

/* welcome */
.intro{left:220px;top:628px;width:760px;text-align:center;font-size:12.5px;line-height:24px;color:var(--muted)}
.feature{width:300px;text-align:center}
.feature h3{font-size:15px;font-weight:600}
.feature p{font-size:12.5px;line-height:24px;color:var(--muted);margin-top:10px}

/* testimonials */
.testi{left:0;top:992px;width:1200px;height:276px;background:linear-gradient(100deg,#2b211a 0%,#5a4636 40%,#8a6a4c 60%,#3a2e24 100%)}
.testi-title{color:var(--white)}
.quote-badge{left:106px;top:1088px;width:108px;height:108px;border-radius:50%;background:var(--white)}
.testi-photo{left:178px;top:1086px;width:112px;height:112px;border-radius:50%;border:4px solid var(--white);background:linear-gradient(#c9c4bd,#6f6a66)}
.testi-text{left:320px;top:1092px;width:720px;color:var(--white);font-style:italic;font-size:13.5px;line-height:25px}
.testi-name{left:320px;top:1184px;color:var(--white);font-size:12.5px;font-weight:700}

/* split blocks */
.split-text{display:flex;flex-direction:column}
.split-head{font-size:21px;font-weight:400;line-height:28px}
.split-head b{font-weight:700}
.split-sub{font-size:13px;font-weight:700;color:var(--blue);margin-top:12px}
.split-body{font-size:12px;line-height:24px;color:#555;margin-top:16px}
.split-body + .split-body{margin-top:22px}
.split-link{font-size:12px;font-weight:700;color:var(--orange);margin-top:16px}

/* consultation */
.consult{left:0;top:1994px;width:1200px;height:196px;background:var(--orange)}
.consult .sec-title{color:var(--white)}
.btn-send{background:var(--blue);color:var(--white);font-weight:700;font-size:13px;display:flex;align-items:center;justify-content:center}

/* agents */
.agent{width:340px;text-align:center}
.agent-photo{width:188px;height:188px;border-radius:50%;border:6px solid #eeeeee;box-shadow:0 0 0 1px #dcdcdc;margin:0 auto}
.agent h4{font-size:15px;font-weight:600;margin-top:28px}
.agent .city{font-size:12px;color:var(--blue);margin-top:2px}
.agent p{font-size:12.5px;line-height:24px;color:var(--muted);margin-top:8px}
.agent .more{font-size:12px;font-weight:700;color:var(--orange);margin-top:10px;display:block}

/* footer */
.footer{left:0;top:2696px;width:1200px;height:309px;background:var(--footer)}
.fcol{color:var(--footer-text)}
.fcol h5{font-size:15px;font-weight:600;color:var(--white);margin-bottom:14px}
.fcol li{list-style:none;font-size:12px;line-height:23.4px;color:var(--footer-text)}
.contact-row{display:flex;gap:18px;font-size:12px;line-height:20px;margin-bottom:22px;color:var(--footer-text)}
.social-row{display:flex;align-items:center;gap:20px;font-size:12px;margin-bottom:16px;color:var(--footer-text)}
.social-box{width:32px;height:32px;background:#d8d8d8}
.copyright{left:0;top:2936px;width:1200px;border-top:1px solid #3c3c3c;text-align:center;font-size:12px;padding-top:20px;color:var(--footer-text)}
</style>
</head>
<body>

<!-- HERO -->
<section class="abs hero" role="img" aria-label="Modern wooden house with terrace and pool at dusk"></section>
<header class="abs nav">
  <div class="brand"><span class="brand-mark"></span>VelnorHomeBridge</div>
  <nav class="menu">
    <svg width="16" height="14" viewBox="0 0 16 14"><path d="M8 0 L16 7 H13 V14 H9.5 V9.5 H6.5 V14 H3 V7 H0 Z" fill="#e9a823"/></svg>
    <span>ABOUT US</span><span>TESTIMONIALS</span><span>SELLERS</span><span>BUYERS</span><span>CONTACT US</span>
    <svg width="16" height="16" viewBox="0 0 16 16"><circle cx="6.5" cy="6.5" r="5" stroke="#fff" stroke-width="2.2" fill="none"/><path d="M10 10 L15 15" stroke="#fff" stroke-width="2.6"/></svg>
    <span class="sign"><svg width="12" height="13" viewBox="0 0 12 13"><circle cx="6" cy="3.5" r="3.3" fill="#fff"/><path d="M0 13 C0 8 12 8 12 13Z" fill="#fff"/></svg>Sign in / Sign Up</span>
  </nav>
</header>
<div class="abs tab tab-buyers">BUYERS</div>
<div class="abs tab tab-sellers">SELLERS</div>
<form class="abs lead-form">
  <h1>FIND THE PERFECT BUYER'S AGENT TODAY</h1>
  <div class="field" style="left:24px;top:74px;width:252px">NAME :</div>
  <div class="field" style="left:288px;top:74px;width:254px">EMAIL :</div>
  <div class="field" style="left:554px;top:74px;width:252px">PHONE :</div>
  <div class="field" style="left:24px;top:126px;width:592px">CITY, STATE OR ZIP</div>
  <div class="btn-find" style="left:628px;top:126px;width:178px">FIND AN AGENT</div>
</form>
<div class="abs dots" style="left:559px;top:477px"><span class="dot on"></span><span class="dot"></span><span class="dot"></span><span class="dot"></span></div>

<!-- WELCOME -->
<h2 class="abs sec-title" style="top:570px">WELCOME TO <b>VELNORHOMEBRIDGE</b></h2>
<svg class="abs swoosh" style="top:602px" viewBox="0 0 100 12"><path d="M0 9 Q50 -2 100 6 Q50 3 0 9Z" fill="#e9a823"/></svg>
<p class="abs intro">Neque porro quisquam est, qui dolorem ipsum quia dolor sit amet, consectetur, adipisci velit, sed quia non numquam eius modi tempora incidunt ut labore et dolore magnam aliquam quaerat voluptatem</p>

<svg class="abs" style="left:202px;top:700px" width="120" height="120" viewBox="0 0 120 120" fill="none" stroke="#e9a823" stroke-width="3">
  <rect x="8" y="84" width="14" height="30"/><rect x="30" y="70" width="14" height="44"/><rect x="52" y="56" width="14" height="58"/><rect x="74" y="42" width="14" height="72"/><rect x="96" y="28" width="14" height="86"/>
  <path d="M6 66 L34 44 L50 50 L82 20 L100 8"/><path d="M88 6 H102 V20"/>
</svg>
<svg class="abs" style="left:538px;top:700px" width="120" height="120" viewBox="0 0 120 120" fill="none" stroke="#e9a823" stroke-width="3">
  <circle cx="60" cy="60" r="54"/><circle cx="60" cy="60" r="45"/><path d="M60 24 V60 H86"/>
</svg>
<svg class="abs" style="left:874px;top:700px" width="120" height="120" viewBox="0 0 120 120" fill="none" stroke="#e9a823" stroke-width="3" stroke-linejoin="round">
  <rect x="40" y="6" width="40" height="48"/>
  <path d="M28 112 V66 H42 V112Z"/>
  <path d="M42 70 C56 62 60 54 60 40 C66 38 72 44 70 58 H92 C100 58 100 70 92 70 C100 72 98 82 90 82 C98 84 96 94 88 94 C94 96 92 106 84 106 H60 L42 102"/>
</svg>

<div class="abs feature" style="left:112px;top:838px"><h3>Top Rated Agents</h3><p>At vero eos et accusamus et iusto odio dign ssid ucimus qui blanditiis praesentium volupta tum deleniti atque corrupti quos</p></div>
<div class="abs feature" style="left:448px;top:838px"><h3>Fast time and hassle</h3><p>At vero eos et accusamus et iusto odio dign ssid ucimus qui blanditiis praesentium volupta tum deleniti atque corrupti quos</p></div>
<div class="abs feature" style="left:784px;top:838px"><h3>No Obligation</h3><p>At vero eos et accusamus et iusto odio dign ssid ucimus qui blanditiis praesentium volupta tum deleniti atque corrupti quos</p></div>

<!-- TESTIMONIALS -->
<section class="abs testi" role="img" aria-label="Warm living room interior in the background"></section>
<h2 class="abs sec-title testi-title" style="top:1028px">CLIENT <b>TESTIMONIALS</b></h2>
<svg class="abs swoosh" style="top:1058px" viewBox="0 0 100 12"><path d="M0 9 Q50 -2 100 6 Q50 3 0 9Z" fill="#e9a823"/></svg>
<div class="abs quote-badge"></div>
<svg class="abs" style="left:120px;top:1122px" width="44" height="40" viewBox="0 0 44 40"><path d="M2 40 V22 C2 10 8 3 18 0 L20 5 C13 8 11 13 11 18 H20 V40Z M24 40 V22 C24 10 30 3 40 0 L42 5 C35 8 33 13 33 18 H42 V40Z" fill="#cfcfcf"/></svg>
<div class="abs testi-photo" role="img" aria-label="Portrait photo of the client"></div>
<p class="abs testi-text">It is a long established fact that a reader will be distracted by the readable content of a page when looking at its layout. The point of using Lorem Ipsum is that it has a more-or-less normal distribution of letters, as opposed to using 'Content here, content here', making it look like readable English.</p>
<div class="abs testi-name">- DAREL OKIMBA</div>
<svg class="abs" style="left:550px;top:1212px" width="10" height="18" viewBox="0 0 10 18"><path d="M9 1 L1 9 L9 17" stroke="#fff" stroke-width="2.4" fill="none"/></svg>
<div class="abs dots" style="left:572px;top:1214px"><span class="dot on"></span><span class="dot"></span><span class="dot"></span></div>
<svg class="abs" style="left:636px;top:1212px" width="10" height="18" viewBox="0 0 10 18"><path d="M1 1 L9 9 L1 17" stroke="#fff" stroke-width="2.4" fill="none"/></svg>

<!-- SELLERS -->
<div class="abs" style="left:0;top:1268px;width:598px;height:364px;background:linear-gradient(180deg,#6b8fb8 0%,#b9c8d8 40%,#e6e6e6 62%,#9aa3a6 100%)" role="img" aria-label="White modern villa with glass walls at sunset"></div>
<div class="abs split-text" style="left:642px;top:1310px;width:420px">
  <h2 class="split-head">FOR <b>SELLERS</b></h2>
  <div class="split-sub">SELL YOUR HOME FASTER</div>
  <p class="split-body">Nam libero tempore, cum soluta nobis est eligendi optio cumque nihil impedit quo minus id quod maxime placeat facere possimus, omnis voluptas assumenda est, omnis dolor repellendus.</p>
  <p class="split-body">Temporibus autem quibusdam et aut officiis debitis aut rerum necessitatibus saepe eveniet ut et voluptates repudiandae sint et molestiae non recusandae. Itaque earum rerum hic tenetur a sapiente delectus, ut aut reiciendis voluptatibus..</p>
  <div class="split-link">FIND YOUR PERFECT AGENT NOW &gt;&gt;</div>
</div>

<!-- BUYERS -->
<div class="abs split-text" style="left:100px;top:1674px;width:460px">
  <h2 class="split-head">FOR <b>BUYERS</b></h2>
  <div class="split-sub">BUY YOUR DREAM HOME</div>
  <p class="split-body">Nam libero tempore, cum soluta nobis est eligendi optio cumque nihil impedit quo minus id quod maxime placeat facere possimus, omnis voluptas assumenda est, omnis dolor repellendus.</p>
  <p class="split-body">Temporibus autem quibusdam et aut officiis debitis aut rerum necessitatibus saepe eveniet ut et voluptates repudiandae sint et molestiae non recusandae. Itaque earum rerum hic tenetur a sapiente delectus, ut aut reiciendis voluptatibus..</p>
  <div class="split-link">FIND YOUR PERFECT AGENT NOW &gt;&gt;</div>
</div>
<div class="abs" style="left:600px;top:1632px;width:600px;height:362px;background:linear-gradient(90deg,#dfe3e4 0%,#c9b8a8 35%,#b0545e 60%,#3c4046 100%)" role="img" aria-label="Happy couple holding keys to their new home"></div>

<!-- CONSULTATION -->
<section class="abs consult">
  <h2 class="abs sec-title" style="top:30px">GET FREE <b>CONSULTATION</b></h2>
  <svg class="abs swoosh" style="top:62px" viewBox="0 0 100 12"><path d="M0 9 Q50 -2 100 6 Q50 3 0 9Z" fill="#ffffff"/></svg>
  <div class="field" style="left:168px;top:116px;width:360px;height:44px">NAME :</div>
  <div class="field" style="left:540px;top:116px;width:360px;height:44px">EMAIL ADDRESS :</div>
  <div class="abs btn-send" style="left:912px;top:116px;width:118px;height:44px">SEND</div>
</section>

<!-- AGENTS -->
<h2 class="abs sec-title" style="top:2236px">OUR TOP <b>AGENTS</b></h2>
<svg class="abs swoosh" style="top:2268px" viewBox="0 0 100 12"><path d="M0 9 Q50 -2 100 6 Q50 3 0 9Z" fill="#e9a823"/></svg>
<div class="abs agent" style="left:94px;top:2322px">
  <div class="agent-photo" style="background:linear-gradient(#e4dccf,#b59a72)" role="img" aria-label="Portrait of agent Marit"></div>
  <h4>Marit</h4><div class="city">Seattle, WA</div>
  <p>Temporibus autem quibusdam et aut offic aut rerum necessitatibus saepe..</p><span class="more">READ MORE &gt;&gt;</span>
</div>
<div class="abs agent" style="left:428px;top:2322px">
  <div class="agent-photo" style="background:linear-gradient(#e8e8e8,#6d6d72)" role="img" aria-label="Portrait of agent Teodor"></div>
  <h4>Teodor</h4><div class="city">Seattle, WA</div>
  <p>Temporibus autem quibusdam et aut offic aut rerum necessitatibus saepe..</p><span class="more">READ MORE &gt;&gt;</span>
</div>
<div class="abs agent" style="left:762px;top:2322px">
  <div class="agent-photo" style="background:linear-gradient(#eeeeee,#7b6656)" role="img" aria-label="Portrait of agent Linnea"></div>
  <h4>Linnea</h4><div class="city">Seattle, WA</div>
  <p>Temporibus autem quibusdam et aut offic aut rerum necessitatibus saepe..</p><span class="more">READ MORE &gt;&gt;</span>
</div>

<!-- FOOTER -->
<footer class="abs footer"></footer>
<div class="abs fcol" style="left:100px;top:2734px"><h5>Company</h5><ul><li>Home</li><li>About us</li><li>Testimonials</li><li>Sellers</li><li>Buyers</li><li>Contact Us</li></ul></div>
<div class="abs fcol" style="left:262px;top:2734px"><h5>Top Agents by City</h5><ul><li>San Diego</li><li>Miami</li><li>Phoenix</li><li>San Jose</li><li>Los Angeles</li><li>Orlando</li></ul></div>
<div class="abs fcol" style="left:484px;top:2734px"><h5>Resources</h5><ul><li>Client Reviews</li><li>For Agents</li><li>For Lenders</li><li>My Agent Finder</li><li>Short Sale Agent Finder</li><li>Charitable Agents</li></ul></div>
<div class="abs fcol" style="left:696px;top:2734px;width:240px">
  <h5>Contact Us</h5>
  <div class="contact-row"><svg width="10" height="14" viewBox="0 0 10 14" style="flex:none;margin-top:3px"><path d="M5 14 C5 14 0 7.5 0 5 A5 5 0 0 1 10 5 C10 7.5 5 14 5 14Z M5 3 A2 2 0 1 0 5 7 A2 2 0 1 0 5 3Z" fill="#ddd" fill-rule="evenodd"/></svg><span>At vero eos et accusamus et iust nissimos ducimus qu</span></div>
  <div class="contact-row"><svg width="12" height="12" viewBox="0 0 12 12" style="flex:none;margin-top:4px"><path d="M2.5 0 L5 3 L3.6 4.6 C4.4 6.3 5.7 7.6 7.4 8.4 L9 7 L12 9.5 L10.5 12 C5 12 0 7 0 1.5Z" fill="#ddd"/></svg><span>1 555 010 4477</span></div>
  <div class="contact-row"><svg width="13" height="10" viewBox="0 0 13 10" style="flex:none;margin-top:5px"><rect width="13" height="10" fill="#ddd"/><path d="M0 0 L6.5 5.5 L13 0" stroke="#2b2b2b" stroke-width="1.3" fill="none"/></svg><span style="text-decoration:underline">info@velnorhomebridge.com</span></div>
</div>
<div class="abs fcol" style="left:984px;top:2734px">
  <h5>Social Media</h5>
  <div class="social-row"><span class="social-box"></span>Friendlane</div>
  <div class="social-row"><span class="social-box"></span>Chirpnet</div>
  <div class="social-row"><span class="social-box"></span>Circleplus</div>
</div>
<div class="abs copyright">Copyright © 2016, VelnorHomeBridge. All rights reserved.</div>

</body>
</html>
```